Carpentry company Needs a business card design

We need a design for a Carpentry / building company, business card. Please think of designs out of the ordinary and try to make it eye catching. Our existing logo will need to be incorporated in the design. However feel free to change the colours of the logo to suit your design. I would like to see some designs with green /black and orange incorporated into it.These are not the only colours accepted and all designs that appeal will be accepted.

Please contact me should you have any questions
Thanks Martin

Target Market(s)

General Public seeking carpentry work

Industry/Entity Type

Business

Contact Information for Business Card

- Current company logo ( colours can be changed)
-Phone number ,
- info@brelvanbuild.com.au
- brelvanbuild.com.au
-the facebook symbol

Font styles to use
Other font styles liked:
• You choose

Requirements
Must have
• Services we provide
• - Renovations
• -Deckings & Pergolas
• -Kitchens
• - Bathrooms
• - Intricate details
Nice to have
• an awesome design
Should not have
• Tools on the business card

```html
<!DOCTYPE html>
<html lang="en">
<head>
<meta charset="utf-8">
<title>Brelvan Build – Business Card</title>
<link rel="stylesheet" href="https://fonts.googleapis.com/css2?family=Lato:wght@400;700&display=swap">
<style>
  :root {
    --backdrop: #2b2b2c;
    --frame: #3e2514;
    --frame-edge: #2a180c;
    --wood-light: #a97b4d;
    --wood-mid: #8a5c34;
    --wood-dark: #5a3820;
    --band-dark: #4a2c16;
    --gold: #e3ad5e;
    --gold-soft: #c99553;
    --ink: #2e1b0e;
    --rule: rgba(40, 22, 10, 0.45);
    --rule-light: rgba(230, 180, 110, 0.18);
  }
  * { box-sizing: border-box; margin: 0; padding: 0; }
  html, body {
    width: 1200px; height: 800px; overflow: hidden;
    background: var(--backdrop);
    font-family: "Lato", sans-serif;
  }
  .canvas {
    width: 1200px; height: 800px;
    display: flex; align-items: center; justify-content: center; gap: 40px;
  }
  .card {
    position: relative;
    width: 560px; height: 320px;
    background: linear-gradient(160deg, var(--frame), var(--frame-edge));
    box-shadow: 0 10px 30px rgba(0,0,0,0.45);
  }
  .card__wood {
    position: absolute; inset: 14px;
    clip-path: polygon(22px 0, 100% 0, 100% 100%, 22px 100%, 0 calc(100% - 22px), 0 22px);
    background: radial-gradient(ellipse at 40% 45%, var(--wood-light) 0%, var(--wood-mid) 55%, var(--wood-dark) 100%);
  }
  .card--back .card__wood {
    clip-path: none; border-radius: 14px;
    background: radial-gradient(ellipse at 45% 50%, var(--wood-mid) 0%, var(--wood-dark) 60%, var(--frame) 100%);
  }

  /* Front */
  .name-tab {
    position: absolute; left: 14px; top: 112px;
    width: 268px; height: 84px;
    border-radius: 0 14px 14px 0;
    background: linear-gradient(180deg, var(--wood-dark), var(--band-dark));
    box-shadow: inset 0 1px 0 var(--rule-light), 0 3px 8px rgba(0,0,0,0.35);
    display: flex; flex-direction: column; align-items: flex-end; justify-content: center;
    padding-right: 26px;
  }
  .name-tab__name { color: var(--gold); font-size: 21px; font-weight: 700; letter-spacing: 0.5px; }
  .name-tab__role { color: var(--gold-soft); font-size: 14px; margin-top: 2px; }

  .contact {
    position: absolute; left: 306px; top: 36px; width: 230px;
    color: var(--gold);
  }
  .brand {
    display: flex; align-items: center; gap: 10px;
    font-size: 26px; font-weight: 700; letter-spacing: 1px;
    color: var(--ink); text-transform: uppercase;
  }
  .brand__mark { width: 14px; height: 14px; background: var(--ink); flex: none; }
  .phone {
    display: flex; align-items: center; gap: 12px;
    font-size: 24px; margin-top: 16px; padding-bottom: 8px;
    border-bottom: 1px solid var(--rule);
  }
  .contact-row {
    display: flex; align-items: center; gap: 12px;
    font-size: 12.5px; padding: 9px 0;
    border-bottom: 1px solid var(--rule);
  }
  .contact-row:last-child { border-bottom: none; line-height: 1.3; }
  .icon { width: 18px; height: 18px; flex: none; fill: none; stroke: var(--gold); stroke-width: 1.6; }
  .phone .icon { width: 18px; height: 28px; }

  /* Back */
  .back-brand {
    position: absolute; left: 60px; top: 150px;
    display: flex; align-items: center; gap: 10px;
    font-size: 24px; font-weight: 700; letter-spacing: 1px;
    color: var(--gold); text-transform: uppercase;
  }
  .back-brand .brand__mark { background: var(--gold); }
  .services {
    position: absolute; left: 330px; top: 64px;
    color: var(--gold); font-size: 15px; line-height: 1.6; list-style: none;
  }
  .services__title { margin-bottom: 2px; }
  .services li.service { padding-left: 14px; }
  .back-web {
    position: absolute; right: 40px; bottom: 32px;
    color: var(--gold-soft); font-size: 12.5px;
  }
</style>
</head>
<body>
<main class="canvas">

  <section class="card card--front" aria-label="Business card front">
    <div class="card__wood" role="img" aria-label="Warm brown wood plank texture"></div>

    <div class="name-tab">
      <p class="name-tab__name">David Martin</p>
      <p class="name-tab__role">Designer</p>
    </div>

    <div class="contact">
      <div class="brand"><span class="brand__mark"></span>Brelvan Build</div>

      <div class="phone">
        <svg class="icon" viewBox="0 0 18 28"><rect x="2" y="1" width="14" height="26" rx="2"/><rect x="5" y="5" width="8" height="8"/><line x1="6" y1="20" x2="12" y2="20"/></svg>
        <span>(555) 010.4821</span>
      </div>

      <div class="contact-row">
        <svg class="icon" viewBox="0 0 18 18"><circle cx="9" cy="9" r="7.5"/><ellipse cx="9" cy="9" rx="3.2" ry="7.5"/><line x1="1.5" y1="9" x2="16.5" y2="9"/></svg>
        <span>brelvanbuild.com.au</span>
      </div>
      <div class="contact-row">
        <svg class="icon" viewBox="0 0 18 18"><rect x="1.5" y="4" width="15" height="10"/><polyline points="1.5,4 9,10 16.5,4"/></svg>
        <span>info@brelvanbuild.com.au</span>
      </div>
      <div class="contact-row">
        <svg class="icon" viewBox="0 0 18 18"><path d="M9 17s-5.5-6-5.5-9.5a5.5 5.5 0 0 1 11 0C14.5 11 9 17 9 17z"/><circle cx="9" cy="7.5" r="2"/></svg>
        <span>48, ALDER ROW,<br>FENWICK, NY 10190</span>
      </div>
    </div>
  </section>

  <section class="card card--back" aria-label="Business card back">
    <div class="card__wood" role="img" aria-label="Dark brown wood plank texture"></div>

    <div class="back-brand"><span class="brand__mark"></span>Brelvan Build</div>

    <ul class="services">
      <li class="services__title">- Services we provide</li>
      <li class="service">- Renovations</li>
      <li class="service">- Deckings &amp; Pergolas</li>
      <li class="service">- Kitchens</li>
      <li class="service">- Bathrooms</li>
      <li class="service">- Intricate details</li>
    </ul>

    <p class="back-web">brelvanbuild.com.au</p>
  </section>

</main>
</body>
</html>
```